依頼詳細
ラックに並べられた時に見えるよう(雑誌のように)タイトルは上部にお願いします。写真を大きめに使ってください。美しい音で心に深くしみわたるような演奏にしたいと思っています。やさしく透明感のあるイメージでお願いします。
記載項目
森川沙織ピアノリサイタル
2014年11月8日(土)/開演18:00(開場17:30)
ソラノ心斎橋音楽サロン゛Brise”(大阪駅前第3ビル1F)
入場料(全自由席)前売:3000円 当日3500円 *未就学児の入場はごご遠慮くださいチケット販売 t* ティーナビ(サンデイストア Sunaターミナル)
お問い合わせ ソラノ心斎橋 大阪市北区曽根崎4丁目7番2(大阪駅前第3ビル1F)Tel. 06-6921-4057 , http://saorimori-piano.example/
後援 浪華音楽学院同窓会《響友会》、近畿鍵盤文化協会/
Program (原語表記のものを添付させていただきました)
モーツァルト/ソナタ第10番ハ長調 K.330
ラヴェル/ソナチネ
ラヴェル/「鏡」より 道化師の朝の歌
シューマン/交響的練習曲Op.13
Profile (添付させていただきました)
サイズ
A4
ページ数
片面
希望イメージ
シンプル 複雑
単色 カラフル
暗い 明るい
日常 高級
遊び心 厳粛
未来的 伝統的
女性的 男性的
希望する色
設定なし
納品ファイル
• イラストレーター形式 (.ai)
• フォトショップ形式 (.psd)
補足説明
写真を3枚添付していますが、どれか1枚を選んで使ってください。写真はイメージに合うようにカットしたり加工してくださって結構です。プログラムも添付しましたが、原語表記なしの日本語表記のみでも結構です。ナチュラルなイメージが希望です。
写真をもう一度添付してみました。
たびたび申し訳ありません。
プロフィール、並びに プログラムのファイルも添付できていなかったようなので、そちらももう一度添付します。
よろしくお願いいたします。
数々のご提案ありがとうございます。
みなさんとてもステキなのですが、私の好みを補足させていただきます。

顔以外のスペースが文字で埋まってしまうのは好きではありません。
「間」というのか、「抜け感」というのでしょうか…適度なスペースがほしいです。
音楽も「音と音のあいだに音楽が存在する」ものです。
こんな写真で申し訳ありませんが、ぜひアーティストとしてのセンス、インスピレーションを発揮してください☆よろしくお願いいたします。
■ 選んだ理由

私が表現したい音のイメージと合っているように思いました。
光のキラキラとしたようなものが入っていて、それが音のキラキラに通じるように思ったのと、透明感が感じられ、また柔らかい雰囲気もあると思います。
それなのに、チラシを見たときの印象が強いので、この提案に決めました。

■ 提案者全員のお礼・コメント

たくさんのご提案ありがとうございました。みなさんとてもステキなので、当選&次点を選ぶのが失礼なくらいでした。自分で考えるようなものとは全く違って、さすがプロのお仕事だなぁと思いました。多くのワガママを聞き入れてくださり、本当にありがとうございました。またお願いしたいと思います。感謝申し上げます。

```html
<!DOCTYPE html>
<html lang="ja">
<head>
<meta charset="utf-8">
<title>森川沙織 ピアノリサイタル</title>
<link rel="stylesheet" href="https://fonts.googleapis.com/css2?family=Shippori+Mincho:wght@400;500&family=Noto+Sans+JP:wght@300;400;500&family=Cormorant+Garamond:wght@400;500&display=swap">
<style>
:root{
  --paper:#fdf8f9;
  --blush:#f6e3ea;
  --rose:#e2457f;
  --rose-deep:#c21e63;
  --ink:#5a4a50;
  --ink-soft:#7d6d73;
  --band-a:#d8336f;
  --band-b:#a8175a;
  --white:#ffffff;
}
*{margin:0;padding:0;box-sizing:border-box}
html,body{width:852px;height:1200px;overflow:hidden;background:var(--paper)}
.flyer{position:relative;width:852px;height:1200px;overflow:hidden;
  background:radial-gradient(circle at 12% 30%,#fff 0,var(--paper) 40%,var(--blush) 100%);
  font-family:"Noto Sans JP",sans-serif;color:var(--ink)}
.portrait{position:absolute;left:250px;top:150px;width:602px;height:990px;
  background:
    linear-gradient(180deg,var(--paper) 0%,rgba(253,248,249,0) 12%),
    linear-gradient(90deg,var(--paper) 0%,rgba(253,248,249,0) 32%),
    radial-gradient(ellipse 30% 18% at 50% 30%,#ecc9ba 0,#dba999 45%,rgba(90,60,60,0) 100%),
    radial-gradient(ellipse 42% 25% at 52% 27%,#4a3234 0,#6b4a48 55%,rgba(120,90,90,0) 100%),
    radial-gradient(ellipse 60% 45% at 40% 90%,#b01c5c 0,#c93a74 50%,rgba(230,170,195,0) 100%),
    linear-gradient(180deg,#f7eaee 0%,#f3e1e7 55%,#ecc7d6 100%)}
.title{position:absolute;left:48px;top:22px;font-family:"Shippori Mincho",serif;color:var(--rose);font-weight:500;line-height:1;z-index:1}
.title .name{display:block;font-size:128px;letter-spacing:10px}
.title .kind{display:block;font-size:88px;letter-spacing:4px;margin-top:18px}
.program{position:absolute;left:57px;top:272px;width:330px}
.program h2{font-family:"Cormorant Garamond",serif;font-weight:500;font-size:20px;color:var(--rose);margin-bottom:14px}
.program li{list-style:none;margin-bottom:26px}
.program .ja{display:block;font-size:14px;color:var(--ink)}
.program .orig{display:block;font-family:"Cormorant Garamond",serif;font-size:12px;color:var(--ink-soft);margin-top:2px}
.profile{position:absolute;left:57px;top:880px;width:270px;font-size:9.5px;line-height:1.7;color:var(--ink-soft)}
.profile h3{font-size:12px;font-weight:500;color:var(--ink);margin-bottom:6px}
.profile h3 span{font-family:"Cormorant Garamond",serif;font-size:12px}
.event{position:absolute;left:560px;top:515px;width:275px;color:var(--ink)}
.date{font-family:"Cormorant Garamond",serif;color:var(--rose);line-height:1;white-space:nowrap}
.date .year{font-size:44px}
.date .md{font-size:80px;margin-left:4px}
.date .dow{display:inline-block;width:28px;height:28px;border-radius:50%;background:var(--rose);color:var(--white);
  font-family:"Noto Sans JP",sans-serif;font-size:15px;text-align:center;line-height:28px;vertical-align:8px;margin-left:4px}
.time{font-size:16px;font-weight:500;margin-top:6px}
.time small{font-size:12px}
.venue{font-size:13px;font-weight:500;margin-top:4px}
.venue small{display:block;font-size:10px;font-weight:400;text-align:right}
.price{font-size:11px;margin-top:30px;line-height:1.6}
.price strong{font-size:14px;font-weight:500}
.price small{display:block;font-size:9px}
.ticket{font-size:13px;margin-top:16px;line-height:1.5}
.ticket small{display:block;font-size:10px}
.contact{position:absolute;left:0;bottom:0;width:852px;height:60px;padding:9px 30px;
  background:linear-gradient(90deg,var(--band-a),var(--band-b));color:var(--white);font-size:11.5px;line-height:1.6}
.contact b{font-weight:500;font-size:13px}
</style>
</head>
<body>
<main class="flyer">
  <div class="portrait" role="img" aria-label="ピアニストのポートレート写真。マゼンタのドレスで微笑む女性、柔らかな光の背景"></div>

  <h1 class="title"><span class="name">森川沙織</span><span class="kind">ピアノリサイタル</span></h1>

  <section class="program">
    <h2>Program</h2>
    <ul>
      <li><span class="ja">モーツァルト／ソナタ第10番ハ長調 K.330</span><span class="orig">W.A.Mozart / Sonate Nr.10 C-dur K.330</span></li>
      <li><span class="ja">ラヴェル／ソナチネ</span><span class="orig">M.Ravel / Sonatine</span></li>
      <li><span class="ja">ラヴェル／「鏡」より 道化師の朝の歌</span><span class="orig">M.Ravel / Miroirs « Alborada del gracioso »</span></li>
      <li><span class="ja">シューマン／交響的練習曲 Op.13</span><span class="orig">R.Schumann / Symphonic Etudes Op.13</span></li>
    </ul>
  </section>

  <section class="profile">
    <h3>プロフィール　森川沙織 ピアノ <span>(Saori Morikawa)</span></h3>
    <p>大阪府出身。4歳よりピアノを始める。音楽大学ピアノ専攻を卒業後、同大学院修了。在学中より各地の演奏会に出演し、ソロのほか室内楽、歌曲伴奏の分野でも活動を重ねる。</p>
    <p>国内のコンクールにて入賞。現在は後進の指導にあたるとともに、サロンコンサートを中心に演奏活動を続けている。透明感のある音色と繊細な表現に定評がある。</p>
  </section>

  <section class="event">
    <p class="date"><span class="year">2014</span><span class="md">11/8</span><span class="dow">土</span></p>
    <p class="time">開演18:00<small>（開場17:30）</small></p>
    <p class="venue">ソラノ心斎橋音楽サロン゛Brise”<small>（浪速中央第5ビル1F）</small></p>
    <p class="price">入場料（全自由席）<strong>前売 3,000円</strong>　<strong>当日 3,500円</strong><small>＊未就学児の入場はご遠慮ください</small></p>
    <p class="ticket">チケット販売 ／ t* ティーナビ<small>（サンデイストア Sunaターミナル）</small></p>
  </section>

  <footer class="contact">
    <p><b>お問い合わせ／ソラノ心斎橋</b>　大阪市北区曽根崎4丁目7番2 浪速中央第5ビル1F　Tel. 06-6921-4057　http://saorimori-piano.example/</p>
    <p>後援：浪華音楽学院同窓会《響友会》　近畿鍵盤文化協会</p>
  </footer>
</main>
</body>
</html>
```